The Core Haven

a business card that we will give to customers, Doctors, Midwifes, surgeons, Pilates and Yoga instructors, chiropractors, physiotherapists.
Our business is based in Australia, Melbourne

Please visit our website to get a better idea about our business www.thecorehaven.com.au

Target Market(s)

health, wellbeing, no surgery, natural healing, medical

Industry/Entity Type

Business

Contact Information for Business Card

Mira Pelloway
Pilates Instructor
0468 273 514

Rosalind Ferriday
Yoga Instructor
0439 615 207

email thecorehaven@mailvora.com
Website www.thecorehaven.com.au

Requirements
Must have
• A classy, sophisticated feel.

front and back
Use of our business Logo (either in black or white)
Use of Varnick Method Logo - this logo must be smaller then our business logo as it is just a contractual legal requirement to have this logo

NOTE: we could not upload more files as this would only let us upload one file - please contact us for the other logo's.
Nice to have
• targeted at both female and male.

Different base colours on each side

our business is about repairing separated abdominals:
Do you have a Bulging belly?
Do you get asked if you are pregnant?
Have been diagnosed with a Diastasis Recti?
Do you Suffer back pain or hip pain?
Weak core strength and weak pelvic floor?
Considering a tummy tuck? (it can be healed without surgery)
Have an umbilical hernia?
An "Outie" belly button that used to be an "Innie"?
Plus we specialise in Pilates and yoga

```html
<!DOCTYPE html>
<html lang="en">
<head>
<meta charset="utf-8">
<title>The Core Haven – Business Card</title>
<link rel="stylesheet" href="https://fonts.googleapis.com/css2?family=Open+Sans:wght@300;400;600;700&display=swap">
<style>
  :root {
    --backdrop: #ebe8e3;
    --charcoal: #58595b;
    --charcoal-deep: #4a4b4d;
    --sky: #a8d3f0;
    --ocean: #1f74b0;
    --coral: #e5322b;
    --mist: #e4e4e4;
    --ink: #58595b;
    --rule: #7a7a7a;
    --paper: #ffffff;
  }
  * { box-sizing: border-box; margin: 0; padding: 0; }
  html, body { width: 1108px; height: 1200px; overflow: hidden; }
  body {
    position: relative;
    background: var(--backdrop);
    font-family: "Open Sans", sans-serif;
  }
  .card {
    position: absolute;
    left: 128px;
    width: 858px;
    height: 482px;
    border-radius: 30px;
    overflow: hidden;
  }
  /* Front */
  .card--front { top: 86px; background: var(--charcoal); }
  .front__texture {
    position: absolute; left: 0; top: 0; width: 340px; height: 360px;
    background: radial-gradient(ellipse at 0% 0%, rgba(255,255,255,0.14), rgba(255,255,255,0) 70%);
  }
  .front__brand {
    position: absolute; left: 60px; top: 175px;
    display: flex; align-items: center; gap: 28px;
  }
  .brand-mark {
    width: 124px; height: 124px; border-radius: 50%;
    border: 6px solid var(--ocean);
    flex: none;
  }
  .brand-name {
    color: var(--sky); font-weight: 400; font-size: 66px; line-height: 1;
    letter-spacing: 0.5px; white-space: nowrap;
  }
  .front__tagline {
    position: absolute; left: 374px; top: 352px;
    color: var(--mist); font-weight: 300; font-size: 26px; letter-spacing: 1px;
  }
  .front__web {
    position: absolute; left: 0; right: 0; top: 432px; text-align: center;
    color: #d4d4d4; font-weight: 300; font-size: 22px; letter-spacing: 2px;
  }
  /* Back */
  .card--back { top: 632px; background: var(--paper); }
  .back__wave { position: absolute; left: 0; top: 0; width: 858px; height: 200px; }
  .back__brand {
    position: absolute; left: 32px; top: 34px;
    display: flex; align-items: center; gap: 16px;
  }
  .back__brand .brand-mark { width: 70px; height: 70px; border-width: 4px; }
  .back__brand .brand-name { font-size: 36px; }
  .back__tagline {
    position: absolute; left: 158px; top: 90px;
    color: var(--mist); font-weight: 400; font-size: 13px; letter-spacing: 0.5px;
  }
  .team {
    position: absolute; top: 212px; left: 0; right: 0;
    display: flex; justify-content: center; align-items: flex-start; gap: 34px;
  }
  .member { text-align: center; color: var(--ink); }
  .member__name { font-weight: 700; font-size: 31px; line-height: 44px; }
  .member__role { font-weight: 400; font-size: 23px; margin-top: 8px; }
  .member__phone { font-weight: 400; font-size: 23px; margin-top: 10px; }
  .team__amp { font-weight: 700; font-size: 31px; line-height: 44px; color: var(--ink); }
  .back__rule {
    position: absolute; left: 20px; right: 28px; top: 396px;
    border-top: 2px solid var(--rule);
  }
  .back__contact {
    position: absolute; left: 20px; top: 422px;
    color: var(--ink); font-size: 21px; font-weight: 400;
  }
  .back__contact .sep { margin: 0 10px; }
  .partner {
    position: absolute; right: 34px; top: 426px;
    color: var(--ink); font-size: 15px; font-weight: 600;
  }
</style>
</head>
<body>
  <section class="card card--front" aria-label="Card front">
    <div class="front__texture" role="img" aria-label="Faint decorative pattern area"></div>
    <div class="front__brand">
      <span class="brand-mark"></span>
      <span class="brand-name">The Core Haven</span>
    </div>
    <p class="front__tagline">ABDOMINAL REHABILITATION</p>
    <p class="front__web">www.thecorehaven.com.au</p>
  </section>

  <section class="card card--back" aria-label="Card back">
    <svg class="back__wave" viewBox="0 0 858 200" aria-hidden="true">
      <path d="M0 0 H858 V110 C760 96 640 92 520 110 C380 132 260 170 120 162 C70 159 30 154 0 150 Z" fill="var(--charcoal)"/>
      <path d="M470 118 C600 88 740 90 858 118 V150 C760 112 620 106 470 118 Z" fill="var(--ocean)"/>
      <path d="M450 112 C590 78 740 80 858 102 V124 C740 94 600 92 450 112 Z" fill="var(--coral)"/>
    </svg>
    <div class="back__brand">
      <span class="brand-mark"></span>
      <span class="brand-name">The Core Haven</span>
    </div>
    <p class="back__tagline">ABDOMINAL REHABILITATION</p>

    <div class="team">
      <div class="member">
        <p class="member__name">Mira Pelloway</p>
        <p class="member__role">Pilates Instructor</p>
        <p class="member__phone">0468 273 514</p>
      </div>
      <span class="team__amp">&amp;</span>
      <div class="member">
        <p class="member__name">Rosalind Ferriday</p>
        <p class="member__role">Yoga Instructor</p>
        <p class="member__phone">0439 615 207</p>
      </div>
    </div>

    <div class="back__rule"></div>
    <p class="back__contact">thecorehaven@mailvora.com<span class="sep">|</span>www.thecorehaven.com.au</p>
    <p class="partner">Varnick Method</p>
  </section>
</body>
</html>
```